Need modern simple design for magazine ad, apartment and condo roofer.

I need a half page magazine ad for a local roofer to publish in an industry magazine. Apartment associations industry. All types of roofs. Shingle and Flat
Need the design to be creative and modern, clean and simple. I do not want a busy design. One that stands out and makes a point quickly.
Logo must be prominent.
DO NOT USE PHOTOS FROM MY WEBSITE PLEASE. Looking for something new.
I work on entire complexes not houses.

Need to make sure our phone number and email address are listed at the bottom. Here is my website www.vorbelan.com
Want to stay away from standard clip arts of tools, homes, apartment buildings.
Half Horizontal 7.25 x 4.75
Ads should be in PDF and JPG format.

Target Market(s)

Apartment or Condo owners looking for large scale roofing projects

Industry/Entity Type

Roofing

Requirements
Must have
• Prominent Logo
Simple Clean Design
Create graphics
Not Busy
Should not have
• Clip Art
No Photos from my website

```html
<!DOCTYPE html>
<html lang="en">
<head>
<meta charset="utf-8">
<title>Vorbelan Roofing – Half Page Ad</title>
<link rel="stylesheet" href="https://fonts.googleapis.com/css2?family=Open+Sans:wght@400;600;700&display=swap">
<style>
  :root {
    --page-bg: #e9e9e9;
    --band-dark: #1f1f1f;
    --band-panel: #2e2e2e;
    --brand-blue: #3f8fd8;
    --ad-blue-top: #2f43b8;
    --ad-blue-bottom: #2437a4;
    --ink-light: #ffffff;
    --rule-light: rgba(255,255,255,0.85);
  }
  * { margin: 0; padding: 0; box-sizing: border-box; }
  html, body {
    width: 1200px; height: 897px; overflow: hidden;
    background: var(--page-bg);
    font-family: "Open Sans", Arial, sans-serif;
  }
  .ad {
    position: absolute; left: 50px; top: 97px;
    width: 1100px; height: 703px;
    overflow: hidden;
  }
  .ad-header {
    position: absolute; left: 0; top: 0; width: 100%; height: 246px;
    background: var(--band-dark);
  }
  .brand-panel {
    position: absolute; left: 105px; top: 0; width: 889px; height: 246px;
    background: var(--band-panel);
    display: flex; align-items: center; justify-content: center; gap: 26px;
  }
  .brand-mark {
    width: 70px; height: 70px; background: var(--brand-blue); flex: none;
  }
  .brand-name {
    color: var(--brand-blue); font-weight: 700; font-size: 80px;
    letter-spacing: 1px; line-height: 1; white-space: nowrap;
  }
  .ad-body {
    position: absolute; left: 0; top: 246px; width: 100%; height: 457px;
    color: var(--ink-light);
  }
  .roof-texture {
    position: absolute; inset: 0;
    background: linear-gradient(180deg, var(--ad-blue-top), var(--ad-blue-bottom));
  }
  .headline {
    position: absolute; left: 0; top: 34px; width: 100%;
    text-align: center; font-weight: 700; font-size: 35px;
  }
  .services-title {
    position: absolute; left: 60px; right: 60px; top: 92px;
    display: flex; align-items: center; gap: 18px;
    font-weight: 700; font-size: 35px;
  }
  .services-title::before, .services-title::after {
    content: ""; flex: 1; height: 2px; background: var(--rule-light);
  }
  .service-list {
    position: absolute; top: 160px; list-style: none;
    font-size: 18.5px; line-height: 23.5px; white-space: nowrap;
  }
  .col-1 { left: 60px; }
  .col-2 { left: 324px; }
  .col-3 { left: 600px; }
  .col-4 { left: 889px; }
  .tagline {
    position: absolute; left: 60px; top: 362px;
    font-size: 23px; white-space: nowrap;
  }
  .contact {
    position: absolute; left: 778px; top: 352px; text-align: left;
    white-space: nowrap;
  }
  .contact-phone { font-weight: 700; font-size: 28px; }
  .contact-web { font-weight: 700; font-size: 17px; margin-top: 0; }
</style>
</head>
<body>
  <section class="ad">
    <header class="ad-header">
      <div class="brand-panel">
        <span class="brand-mark" aria-hidden="true"></span>
        <span class="brand-name">Vorbelan Roofing</span>
      </div>
    </header>

    <div class="ad-body">
      <div class="roof-texture" role="img" aria-label="Close-up of blue metal roof panels"></div>

      <h1 class="headline">More than 30 years experience</h1>
      <h2 class="services-title">Services:</h2>

      <ul class="service-list col-1">
        <li>Design Builds</li>
        <li>Siding / Wood Replacement</li>
        <li>Doors &amp; Windows</li>
        <li>Full Paint</li>
        <li>Roofing (all types)</li>
        <li>Balcony/Landing Repairs</li>
        <li>Gutters</li>
      </ul>
      <ul class="service-list col-2">
        <li>Brick/Stucco/Masonry</li>
        <li>Carports / Metal Fencing</li>
        <li>Fire Restoration</li>
        <li>Concrete ADA</li>
        <li>Consulting</li>
        <li>Due Diligence</li>
        <li>Interior Renovations</li>
      </ul>
      <ul class="service-list col-3">
        <li>Balcony/Landing Repairs</li>
        <li>Leasing Office Renovations</li>
        <li>Electrical</li>
        <li>Foundation Repairs</li>
        <li>HVAC</li>
        <li>Sidewalk / Driveway Repairs</li>
        <li>Retaining Walls</li>
      </ul>
      <ul class="service-list col-4">
        <li>Decorative Fencing</li>
        <li>Adult Centers</li>
        <li>Playgrounds</li>
        <li>and more. .</li>
      </ul>

      <p class="tagline">No job is too small or too big for our knowledgeable crews.</p>
      <div class="contact">
        <p class="contact-phone">Call us: 555.014.2290</p>
        <p class="contact-web">www.vorbelan.com</p>
      </div>
    </div>
  </section>
</body>
</html>
```